Business card design needed

Double sided
Color, unique, elegant

Maybe put this quote somewhere?? But I think it might make it to cluttered?
“The Pilates Method of Body
Conditioning develops the body
uniformly, corrects posture, restores
vitality, invigorates the mind and
elevates the spirit”
- Henrik Dovacombe

Industry/Entity Type

Business

Contact Information for Business Card

Marta Kellbrook
Pilates Instructor & Personal trainer
Mobile: 0498265043
www.lorvix.com.au
email: lorvixhealth.fitness@qentamail.com

```html
<!DOCTYPE html>
<html lang="en">
<head>
<meta charset="utf-8">
<title>Lorvix Health and Fitness – Business Card</title>
<link rel="stylesheet" href="https://fonts.googleapis.com/css2?family=Marcellus&family=Raleway:wght@300&display=swap">
<style>
  :root {
    --page-bg: #e9e7e3;
    --card-navy: #07091f;
    --card-deep: #0c1147;
    --card-glow: #3a4fd6;
    --card-streak: #6f7ff0;
    --quote-ink: #f3e6f2;
    --name-red: #e5473a;
    --contact-ink: #f2f2f6;
    --brand-grey: #5f6470;
    --brand-accent: #d77fc4;
  }
  * { margin: 0; padding: 0; box-sizing: border-box; }
  html, body { width: 1200px; height: 1129px; overflow: hidden; }
  body {
    background: var(--page-bg);
    position: relative;
    font-family: "Marcellus", Georgia, serif;
  }
  .card {
    position: absolute;
    left: 160px;
    width: 880px;
    height: 503px;
    border-radius: 6px;
    overflow: hidden;
    box-shadow: 0 10px 30px rgba(0,0,0,0.25);
    background:
      radial-gradient(ellipse 55% 22% at 62% 38%, rgba(111,127,240,0.55), transparent 70%),
      radial-gradient(ellipse 70% 40% at 50% 55%, rgba(58,79,214,0.6), transparent 75%),
      linear-gradient(160deg, var(--card-navy) 0%, var(--card-deep) 50%, var(--card-navy) 100%);
  }
  .card--quote { top: 40px; }
  .card--contact { top: 586px; }

  .light-streaks { position: absolute; inset: 0; }

  /* Quote side */
  .brand-block {
    position: absolute;
    left: 70px;
    top: 170px;
    display: flex;
    flex-direction: column;
    gap: 6px;
  }
  .brand-row { display: flex; align-items: center; gap: 16px; }
  .brand-dot {
    width: 26px; height: 26px; border-radius: 50%;
    background: var(--brand-accent);
  }
  .brand-name {
    font-family: "Raleway", Arial, sans-serif;
    font-weight: 300;
    font-size: 64px;
    letter-spacing: 4px;
    color: var(--brand-grey);
  }
  .brand-tagline {
    font-family: "Raleway", Arial, sans-serif;
    font-weight: 300;
    font-size: 24px;
    color: var(--brand-grey);
    padding-left: 42px;
  }
  .quote {
    position: absolute;
    left: 450px;
    top: 40px;
    font-size: 27px;
    line-height: 1.05;
    color: var(--quote-ink);
  }
  .quote-author { padding-left: 28px; }

  /* Contact side */
  .person-name {
    position: absolute;
    left: 0; right: 0;
    top: 120px;
    text-align: center;
    font-size: 44px;
    color: var(--name-red);
  }
  .person-role {
    position: absolute;
    left: 0; right: 0;
    top: 178px;
    text-align: center;
    font-size: 31px;
    color: var(--name-red);
  }
  .contact-list {
    position: absolute;
    left: 180px;
    top: 250px;
    list-style: none;
    color: var(--contact-ink);
    font-size: 22px;
    line-height: 1.2;
  }
  .contact-list .mobile { font-size: 25px; margin-bottom: 4px; }
  .corner-brand {
    position: absolute;
    right: 40px;
    bottom: 40px;
    display: flex;
    align-items: center;
    gap: 8px;
  }
  .corner-brand .brand-dot { width: 12px; height: 12px; }
  .corner-brand .brand-name { font-size: 20px; letter-spacing: 1px; }
</style>
</head>
<body>

<section class="card card--quote" aria-label="Business card, quote side">
  <svg class="light-streaks" viewBox="0 0 880 503" preserveAspectRatio="none" aria-hidden="true">
    <path d="M0 330 C 220 260, 420 170, 880 120" stroke="var(--card-streak)" stroke-opacity="0.35" stroke-width="3" fill="none"/>
    <path d="M0 380 C 260 300, 480 230, 880 200" stroke="var(--card-glow)" stroke-opacity="0.4" stroke-width="2" fill="none"/>
  </svg>
  <div class="brand-block">
    <div class="brand-row">
      <span class="brand-dot"></span>
      <span class="brand-name">LORVIX</span>
    </div>
    <span class="brand-tagline">Health and fitness</span>
  </div>
  <blockquote class="quote">
    “The Pilates Method of<br>
    Body<br>
    Conditioning develops the<br>
    body<br>
    uniformly, corrects posture,<br>
    restores<br>
    vitality, invigorates the mind<br>
    and<br>
    elevates the spirit”<br>
    <span class="quote-author">- Henrik Dovacombe</span>
  </blockquote>
</section>

<section class="card card--contact" aria-label="Business card, contact side">
  <svg class="light-streaks" viewBox="0 0 880 503" preserveAspectRatio="none" aria-hidden="true">
    <path d="M0 200 C 240 150, 520 120, 880 60" stroke="var(--card-streak)" stroke-opacity="0.35" stroke-width="3" fill="none"/>
    <path d="M0 260 C 300 210, 560 180, 880 150" stroke="var(--card-glow)" stroke-opacity="0.4" stroke-width="2" fill="none"/>
  </svg>
  <h1 class="person-name">Marta Kellbrook</h1>
  <p class="person-role">Pilates Instructor &amp; Personal trainer</p>
  <ul class="contact-list">
    <li class="mobile">Mobile: 0498265043</li>
    <li>www.lorvix.com.au</li>
    <li>email: lorvixhealth.fitness@qentamail.com</li>
  </ul>
  <div class="corner-brand">
    <span class="brand-dot"></span>
    <span class="brand-name">LORVIX</span>
  </div>
</section>

</body>
</html>
```